Bramwell Pocket Mate App

We need a brand and design for our "Bramwell Pocket Mate" app.

- Provide a design, icon for a snow guide app.

App is for snowboarders, skiers and provides details on ski fields, resorts, snow reports, maps, accom, news, weather and trail maps.

4x designs should be provided in the following sizes...

Navigation bar background - for top header of the app.
1080x135px

Application icon
120x120px

Launch image - should have logo and an inspiring illustration/photo
640x920px
640x1096px (Tavora 5)

Home image - this is the background image and will have a row of icons at the bottom.
640x920px
640x1096px (Tavora 5)

Icons - A range of snow/ski type icons should be provided. These will be used as App links from the homepage for links such as..... snow reports, weather, ski resorts, accom, news, gear, info, snow, trail maps..... (see attached example) Note: these icons should work nicely when sitting on the home image. Be clear and stand to the front of the app like the homescreen of an Tavora.

Colours should be solid and flat design feel. The colors should reflect snow / winter / cool. A primary color should be selected for links.

An ideal for the splash screens is for a snowboarder and skier silhouette standing next to each other at the top of a run looking down into the valley of a ski resort. Rolling mountains in the distance etc ! This is only an idea so don't limit your creativity.

Have fun and good luck!

```html
<!DOCTYPE html>
<html lang="en">
<head>
<meta charset="utf-8">
<title>Bramwell Pocket Mate – App Screens</title>
<link rel="stylesheet" href="https://fonts.googleapis.com/css2?family=Arimo:wght@400;700&family=Lato:wght@400&display=swap">
<style>
  :root {
    --page: #ffffff;
    --sky: #9ae7ee;
    --brand: #00aeef;
    --label: #12d2ea;
    --nav: #93e0e8;
    --action: #3fa9f0;
    --panel: #e4e4e4;
    --tab: #eeeeee;
    --rule: #cfcfcf;
    --key-text: #8a8a8a;
    --key: #c2c2c2;
    --ink: #111111;
    --snow-light: #f5f5f5;
    --snow-mid: #ededed;
    --snow-deep: #e5e5e5;
    --icon-top: #a9e6f7;
    --icon-bottom: #08b2f0;
  }
  * { box-sizing: border-box; margin: 0; padding: 0; }
  html, body { width: 1200px; height: 1000px; overflow: hidden; background: var(--page); }
  body { position: relative; font-family: "Arimo", Arial, sans-serif; }

  .screen { position: absolute; overflow: hidden; }
  .screen-label {
    position: absolute; font-family: "Lato", "Gill Sans", sans-serif; font-weight: 400;
    font-size: 70px; line-height: 1; color: var(--label); text-align: center; letter-spacing: -3px;
  }
  .screen-label.icon-label { letter-spacing: 0; }

  /* Launch screen */
  .launch { left: 85px; top: 26px; width: 349px; height: 615px; background: var(--sky); }
  .launch-mark { position: absolute; left: 126px; top: 146px; width: 96px; height: 96px; border-radius: 50%; background: var(--brand); }
  .launch-name { position: absolute; left: 0; right: 0; top: 292px; text-align: center; font-weight: 700; font-size: 23px; color: var(--brand); }
  .launch-scene { position: absolute; left: 0; top: 356px; width: 349px; height: 259px; }

  /* Menu screen */
  .menu { left: 487px; top: 26px; width: 345px; height: 615px; background: #fff; border-bottom: 1px solid #777; }
  .status-bar { position: absolute; left: 0; top: 0; width: 345px; height: 25px; background: linear-gradient(#ffffff, #e9f3f3); border-top: 1px solid #333; font-size: 12px; font-weight: 700; }
  .status-bar .carrier { position: absolute; left: 5px; top: 5px; letter-spacing: 0.5px; }
  .status-bar .wifi { position: absolute; left: 99px; top: 6px; }
  .status-bar .time { position: absolute; left: 147px; top: 5px; }
  .status-bar .battery { position: absolute; right: 6px; top: 8px; width: 26px; height: 9px; background: #000; border-radius: 2px; }
  .nav-bar { position: absolute; left: 0; top: 25px; width: 345px; height: 47px; background: var(--nav); }
  .nav-title { position: absolute; left: 0; right: 0; top: 12px; text-align: center; color: #fff; font-weight: 700; font-size: 18px; }
  .nav-back { position: absolute; left: 10px; top: 8px; width: 98px; height: 32px; }
  .nav-close { position: absolute; left: 253px; top: 10px; width: 81px; height: 32px; background: #fff; border-radius: 5px; color: var(--label); font-weight: 700; font-size: 14px; text-align: center; line-height: 32px; }
  .search-row { position: absolute; left: 0; top: 72px; width: 345px; height: 55px; background: var(--panel); }
  .search-field { position: absolute; left: 7px; top: 11px; width: 235px; height: 33px; background: #fff; border-radius: 10px; }
  .search-button { position: absolute; left: 253px; top: 11px; width: 84px; height: 30px; background: var(--action); border-radius: 10px; color: #fff; font-size: 13px; text-align: center; line-height: 30px; }
  .tabs { position: absolute; left: 0; top: 127px; width: 345px; height: 47px; display: flex; border-top: 1px solid var(--rule); border-bottom: 1px solid var(--rule); }
  .tab { flex: 1; background: var(--tab); border-right: 2px solid var(--rule); color: #666; font-size: 15px; text-align: center; line-height: 45px; }
  .tab:last-child { border-right: 1px solid var(--rule); }
  .place-list { position: absolute; left: 16px; top: 174px; width: 329px; list-style: none; }
  .place-list li { height: 49px; border-bottom: 2px solid #d5d5d5; font-size: 16px; color: var(--ink); line-height: 49px; position: relative; }
  .place-list svg { position: absolute; right: 15px; top: 18px; }
  .keyboard { position: absolute; left: 0; top: 382px; width: 345px; height: 233px; background: var(--panel); color: var(--key-text); font-size: 24px; }
  .key-row { position: absolute; display: flex; }
  .key-row span { text-align: center; }
  .key-pad { position: absolute; background: var(--key); border-radius: 5px; }

  /* Icon */
  .app-icon { position: absolute; left: 882px; top: 221px; width: 226px; height: 226px; border-radius: 36px; overflow: hidden; background: linear-gradient(#1fc0f2, var(--icon-bottom)); }
  .app-icon-gloss { position: absolute; left: 0; top: 0; width: 226px; height: 120px; }
  .app-icon-mark { position: absolute; left: 73px; top: 48px; width: 80px; height: 80px; border-radius: 50%; background: #fff; }
  .app-icon-name { position: absolute; left: 0; right: 0; top: 146px; text-align: center; color: #fff; font-weight: 700; font-size: 19px; line-height: 24px; }
</style>
</head>
<body>

  <section class="screen launch">
    <div class="launch-mark"></div>
    <div class="launch-name">Bramwell Pocket Mate</div>
    <svg class="launch-scene" viewBox="0 0 349 259" role="img" aria-label="Rolling snow hills with an igloo, polar bears, pine trees and snowboarders jumping">
      <path d="M0 84 C110 100 230 78 349 28 L349 259 L0 259 Z" fill="var(--snow-light)"/>
      <path d="M0 104 C110 92 220 112 349 58 L349 259 L0 259 Z" fill="var(--snow-mid)"/>
      <path d="M0 116 C120 104 220 150 349 92" fill="none" stroke="#ffffff" stroke-width="6" opacity="0.7"/>
      <path d="M0 132 C80 120 170 126 240 150 C285 162 320 140 349 122 L349 259 L0 259 Z" fill="#e9e9e9"/>
      <path d="M0 140 C90 128 180 140 245 156" fill="none" stroke="#ffffff" stroke-width="4" opacity="0.6"/>
      <rect x="0" y="154" width="349" height="105" fill="var(--snow-deep)"/>
    </svg>
  </section>
  <div class="screen-label" style="left:85px; width:349px; top:672px;">LAUNCH</div>

  <section class="screen menu">
    <div class="status-bar">
      <span class="carrier">●●●●● DRIFT</span>
      <svg class="wifi" width="14" height="11" viewBox="0 0 14 11">
        <path d="M1 4 A9 9 0 0 1 13 4" fill="none" stroke="#222" stroke-width="1.6"/>
        <path d="M3.5 6.5 A5.5 5.5 0 0 1 10.5 6.5" fill="none" stroke="#222" stroke-width="1.6"/>
        <circle cx="7" cy="9.3" r="1.4" fill="#222"/>
      </svg>
      <span class="time">9:41 A.M</span>
      <span class="battery"></span>
    </div>
    <header class="nav-bar">
      <svg class="nav-back" viewBox="0 0 98 32">
        <path d="M12 0 H97 V32 H12 L0 16 Z" fill="#fff"/>
        <text x="50" y="22" text-anchor="middle" font-family="Arimo, Arial, sans-serif" font-weight="700" font-size="15" fill="#12d2ea">Back</text>
      </svg>
      <div class="nav-title">Maps</div>
      <div class="nav-close">Close</div>
    </header>
    <div class="search-row">
      <div class="search-field"></div>
      <div class="search-button">Search</div>
    </div>
    <nav class="tabs">
      <div class="tab">Friends</div>
      <div class="tab">History</div>
      <div class="tab">Mark</div>
    </nav>
    <ul class="place-list">
      <li>Himalaya<svg width="8" height="13" viewBox="0 0 8 13"><path d="M1 1 L6.5 6.5 L1 12" fill="none" stroke="#b5b5b5" stroke-width="2"/></svg></li>
      <li>Utah<svg width="8" height="13" viewBox="0 0 8 13"><path d="M1 1 L6.5 6.5 L1 12" fill="none" stroke="#b5b5b5" stroke-width="2"/></svg></li>
      <li>France<svg width="8" height="13" viewBox="0 0 8 13"><path d="M1 1 L6.5 6.5 L1 12" fill="none" stroke="#b5b5b5" stroke-width="2"/></svg></li>
      <li>Holland<svg width="8" height="13" viewBox="0 0 8 13"><path d="M1 1 L6.5 6.5 L1 12" fill="none" stroke="#b5b5b5" stroke-width="2"/></svg></li>
    </ul>
    <div class="keyboard">
      <div class="key-row" style="left:8px; top:18px; width:332px; justify-content:space-between;">
        <span>1</span><span>2</span><span>3</span><span>4</span><span>5</span><span>6</span><span>7</span><span>8</span><span>9</span><span>0</span>
      </div>
      <div class="key-row" style="left:10px; top:58px; width:325px; justify-content:space-between;">
        <span>Q</span><span>W</span><span>E</span><span>R</span><span>T</span><span>Y</span><span>U</span><span>I</span><span>O</span><span>P</span>
      </div>
      <div class="key-row" style="left:23px; top:98px; width:300px; justify-content:space-between;">
        <span>A</span><span>S</span><span>D</span><span>F</span><span>G</span><span>H</span><span>J</span><span>K</span><span>L</span>
      </div>
      <div class="key-pad" style="left:4px; top:133px; width:51px; height:30px;"></div>
      <div class="key-row" style="left:65px; top:134px; width:215px; justify-content:space-between;">
        <span>Z</span><span>X</span><span>C</span><span>V</span><span>B</span><span>N</span><span>M</span>
      </div>
      <div class="key-pad" style="left:289px; top:133px; width:52px; height:30px;"></div>
      <div class="key-pad" style="left:5px; top:181px; width:26px; height:30px;"></div>
      <div class="key-pad" style="left:37px; top:181px; width:26px; height:30px;"></div>
      <div class="key-pad" style="left:69px; top:181px; width:206px; height:30px;"></div>
      <div class="key-pad" style="left:282px; top:181px; width:25px; height:30px;"></div>
      <div class="key-pad" style="left:314px; top:181px; width:26px; height:30px;"></div>
    </div>
  </section>
  <div class="screen-label" style="left:487px; width:272px; top:672px;">MENU</div>

  <div class="app-icon">
    <svg class="app-icon-gloss" viewBox="0 0 226 120">
      <defs>
        <linearGradient id="gloss" x1="0" y1="0" x2="0" y2="1">
          <stop offset="0" stop-color="#b6ebf9"/>
          <stop offset="1" stop-color="#5fd0f4"/>
        </linearGradient>
      </defs>
      <path d="M0 0 H226 V30 C170 85 60 90 0 40 Z" fill="url(#gloss)"/>
    </svg>
    <div class="app-icon-mark"></div>
    <div class="app-icon-name">Bramwell<br>Pocket Mate</div>
  </div>
  <div class="screen-label icon-label" style="left:882px; width:226px; top:478px;">ICON</div>

</body>
</html>
```